The Quiet Lantern - The best guide in your pocket

The Quiet Lantern (فانوس‌آرام in Persian)

We need a new app design for a major update on Android, iOS and Windows Universal platforms.
Our company works on creating innovative apps and games on different platforms, this particular app is free for end users and provides location based services. Here is the abstract feature list:
• Nearest points around user (explore on map or find) including locations, events and skills
• Add points to our database (partners) plus comments and ratings
• Point owners can modify or complete their points data, provide sale events, services and …

Attachments:
Our service logo
The detailed descriptions of different sections (PDF documents)
Updates

Project Deadline Extended Reason: We want more designs :)Give us previews on Home and Map sections at least (more interesting if previews are provided for more sections) Added Saturday, January 7, 2017

Target Market(s)

Public

Industry/Entity Type

Android

Font styles to use
Serif
Sans Serif

Requirements
Must have
• Consider attached service logo & wireframe
• Designs for attached sections
• Fluent user experience
• Modern design
Nice to have
• Right to Left layouts
Should not have
• No alphabet in graphic assets

```html
<!DOCTYPE html>
<html lang="en">
<head>
<meta charset="utf-8">
<title>The Quiet Lantern – App Screens</title>
<link href="https://fonts.googleapis.com/css2?family=Oswald:wght@400;500&family=Roboto:wght@400;500&family=Vazirmatn:wght@400&display=swap" rel="stylesheet">
<style>
  :root{
    --bg-top:#74cfc6;
    --bg-bottom:#4b6e80;
    --header:#3e6472;
    --header-dark:#2e4d5a;
    --panel:#2c4a57;
    --card:#365a68;
    --map:#d3ece8;
    --map-soft:#c2e2dd;
    --accent:#5fbdb2;
    --white:#ffffff;
    --field-text:#9fd3cc;
    --pin-orange:#f48a1c;
    --pin-blue:#1f5fd0;
    --pin-pink:#ec2f8c;
    --star:#f7d51d;
    --text-light:#e6f1f2;
  }
  *{box-sizing:border-box;margin:0;padding:0}
  html,body{width:950px;height:1200px;overflow:hidden}
  body{
    background:linear-gradient(160deg,var(--bg-top),var(--bg-bottom) 70%);
    font-family:"Roboto",sans-serif;
    position:relative;
  }
  .screen{
    position:absolute;top:160px;width:410px;height:880px;
    background:var(--map);overflow:hidden;
    box-shadow:0 20px 40px rgba(0,0,0,.25);
  }
  .screen--home{left:45px}
  .screen--map{left:495px}

  .app-header{
    position:absolute;left:0;top:0;width:100%;height:100px;
    background:var(--header);
  }
  .menu-icon{position:absolute;left:16px;top:36px;width:26px;height:22px}
  .search-field{
    position:absolute;left:56px;top:22px;width:296px;height:52px;
    background:var(--white);box-shadow:0 3px 8px rgba(0,0,0,.25);
    font-family:"Vazirmatn",sans-serif;font-size:15px;color:var(--field-text);
    direction:rtl;text-align:right;padding:14px 14px;
  }
  .search-icon{position:absolute;right:16px;top:34px;width:26px;height:26px}

  .map-area{position:absolute;left:0;width:100%;background:
    linear-gradient(135deg,var(--map) 0%,var(--map-soft) 50%,var(--map) 100%);}
  .screen--home .map-area{top:100px;height:500px}
  .screen--map .map-area{top:140px;height:510px}

  .pin{position:absolute;width:30px;height:40px}
  .pin--user{width:28px;height:38px}

  .categories-band{
    position:absolute;left:0;top:600px;width:100%;height:60px;
    background:var(--header);color:var(--white);
    font-family:"Oswald",sans-serif;font-weight:500;font-size:22px;
    text-align:center;line-height:60px;letter-spacing:.5px;
  }
  .ad-banner{
    position:absolute;left:10px;top:662px;width:390px;height:116px;
    background:linear-gradient(100deg,#d9681a,#f6c419 45%,#f0a21a 75%,#d9531a);
  }
  .ad-label{
    position:absolute;right:30px;bottom:8px;color:var(--white);
    font-family:"Oswald",sans-serif;font-size:9px;letter-spacing:.5px;
  }
  .bottom-dock{position:absolute;left:0;top:780px;width:100%;height:100px;background:var(--panel)}
  .handle-row{position:absolute;left:0;width:100%;height:22px}
  .handle{position:absolute;left:110px;top:8px;width:140px;height:5px;border-radius:3px;background:#5a7d8a}
  .handle-line{position:absolute;left:250px;top:10px;width:60px;height:1px;background:#5a7d8a}
  .comments-label{
    position:absolute;right:12px;top:3px;font-family:"Oswald",sans-serif;
    font-size:11px;color:var(--accent);letter-spacing:.5px;
  }
  .category-row{position:absolute;left:8px;top:24px;display:flex;gap:8px}
  .category{
    width:58px;height:70px;background:var(--card);border-radius:3px;
    display:flex;flex-direction:column;align-items:center;padding-top:6px;
  }
  .category-tile{width:40px;height:40px;background:#cfeae7;border-radius:4px;display:flex;align-items:center;justify-content:center}
  .category-name{font-family:"Oswald",sans-serif;font-size:11px;color:var(--white);margin-top:5px}

  .tabs{
    position:absolute;left:0;top:100px;width:100%;height:40px;background:var(--header-dark);
    display:flex;justify-content:space-between;align-items:center;padding:0 0 0 30px;
    font-family:"Oswald",sans-serif;font-size:12px;color:var(--text-light);letter-spacing:.6px;
  }
  .tab--active{position:relative}
  .tab--active::after{content:"";position:absolute;left:50%;bottom:-14px;margin-left:-6px;
    border:6px solid transparent;border-bottom-color:var(--map)}
  .tab--cut{margin-right:-14px}

  .point-tooltip{
    position:absolute;left:170px;top:240px;width:100px;height:70px;
    background:#8fd3c9;border-radius:4px;padding:7px 8px;
    font-family:"Vazirmatn",sans-serif;font-size:6.5px;line-height:1.55;color:var(--header-dark);
    direction:rtl;text-align:right;box-shadow:0 3px 6px rgba(0,0,0,.2);
  }
  .point-tooltip::before{content:"";position:absolute;left:-8px;top:22px;
    border:5px solid transparent;border-right:8px solid #8fd3c9;border-left:0}

  .comments-panel{position:absolute;left:0;top:650px;width:100%;height:230px;background:var(--panel)}
  .comment-card{
    position:absolute;left:8px;width:394px;height:96px;background:var(--card);
    border-radius:4px;padding:10px 40px 8px 14px;color:var(--text-light);
  }
  .comment-card--one{top:26px}
  .comment-card--two{top:128px}
  .comment-head{display:flex;justify-content:flex-end;align-items:center;gap:8px;margin-bottom:4px}
  .stars{color:var(--star);font-size:12px;letter-spacing:1px}
  .place-name{font-family:"Oswald",sans-serif;font-size:11px;font-weight:500;color:var(--white)}
  .comment-text{font-size:8px;line-height:1.4;color:var(--text-light)}
  .comment-pin{position:absolute;right:10px;top:38px;width:22px;height:30px}
</style>
</head>
<body>

<svg width="0" height="0" style="position:absolute">
  <defs>
    <symbol id="pin-shape" viewBox="0 0 30 40">
      <path d="M15 0C6.7 0 0 6.7 0 15c0 10.5 15 25 15 25s15-14.5 15-25C30 6.7 23.3 0 15 0z" fill="currentColor"/>
      <circle cx="15" cy="15" r="6" fill="#ffffff" opacity=".85"/>
    </symbol>
    <symbol id="menu-shape" viewBox="0 0 26 22">
      <rect y="1" width="26" height="3" fill="#cfe8e6"/>
      <rect y="9" width="26" height="3" fill="#cfe8e6"/>
      <rect y="17" width="26" height="3" fill="#cfe8e6"/>
    </symbol>
    <symbol id="search-shape" viewBox="0 0 26 26">
      <circle cx="10.5" cy="10.5" r="7.5" fill="none" stroke="#cfe8e6" stroke-width="3"/>
      <line x1="16" y1="16" x2="24" y2="24" stroke="#cfe8e6" stroke-width="3.5" stroke-linecap="round"/>
    </symbol>
  </defs>
</svg>

<!-- Home screen -->
<section class="screen screen--home">
  <header class="app-header">
    <svg class="menu-icon"><use href="#menu-shape"/></svg>
    <div class="search-field">جستجوی نزدیک...</div>
    <svg class="search-icon"><use href="#search-shape"/></svg>
  </header>

  <div class="map-area" role="img" aria-label="Map of the Isfahan region with nearby points"></div>
  <svg class="pin" style="left:240px;top:245px;color:#f6b46a"><use href="#pin-shape"/></svg>
  <svg class="pin pin--user" style="left:192px;top:368px;color:#2e5a68"><use href="#pin-shape"/></svg>
  <svg class="pin" style="left:112px;top:418px;color:var(--pin-orange)"><use href="#pin-shape"/></svg>
  <svg class="pin" style="left:68px;top:512px;color:var(--pin-blue)"><use href="#pin-shape"/></svg>
  <svg class="pin" style="left:240px;top:510px;color:var(--pin-pink)"><use href="#pin-shape"/></svg>

  <div class="categories-band">MORE CATEGORIES</div>

  <div class="ad-banner" role="img" aria-label="Advertising banner for an upcoming desert party event">
    <span class="ad-label">ADVERTISING</span>
  </div>

  <div class="bottom-dock">
    <div class="handle-row">
      <span class="handle"></span><span class="handle-line"></span>
      <span class="comments-label">COMMENTS</span>
    </div>
    <div class="category-row">
      <div class="category"><div class="category-tile"><svg width="20" height="27" style="color:#2b7fd8"><use href="#pin-shape"/></svg></div><span class="category-name">School</span></div>
      <div class="category"><div class="category-tile"><svg width="20" height="27" style="color:#2b7fd8"><use href="#pin-shape"/></svg></div><span class="category-name">Parties</span></div>
      <div class="category"><div class="category-tile"><svg width="20" height="27" style="color:#2b7fd8"><use href="#pin-shape"/></svg></div><span class="category-name">eShop</span></div>
      <div class="category"><div class="category-tile"><svg width="20" height="27" style="color:#2b7fd8"><use href="#pin-shape"/></svg></div><span class="category-name">School</span></div>
      <div class="category"><div class="category-tile"><svg width="20" height="27" style="color:#2b7fd8"><use href="#pin-shape"/></svg></div><span class="category-name">Parties</span></div>
      <div class="category"><div class="category-tile"><svg width="20" height="27" style="color:#2b7fd8"><use href="#pin-shape"/></svg></div><span class="category-name">eShop</span></div>
    </div>
  </div>
</section>

<!-- Map screen -->
<section class="screen screen--map">
  <header class="app-header">
    <svg class="menu-icon"><use href="#menu-shape"/></svg>
    <div class="search-field">جستجوی نزدیک...</div>
    <svg class="search-icon"><use href="#search-shape"/></svg>
  </header>
  <nav class="tabs">
    <span class="tab tab--active">LOCATIONS</span>
    <span class="tab">EVENTS</span>
    <span class="tab">SKILLS</span>
    <span class="tab tab--cut">SCHOOLS</span>
  </nav>

  <div class="map-area" role="img" aria-label="Map of the Isfahan region with location points"></div>
  <svg class="pin" style="left:250px;top:150px;color:var(--pin-orange)"><use href="#pin-shape"/></svg>
  <svg class="pin" style="left:132px;top:262px;color:var(--pin-orange)"><use href="#pin-shape"/></svg>
  <svg class="pin" style="left:84px;top:345px;color:var(--pin-blue)"><use href="#pin-shape"/></svg>
  <svg class="pin" style="left:248px;top:415px;color:var(--pin-pink)"><use href="#pin-shape"/></svg>
  <div class="point-tooltip">مکانی آرام برای شام خانوادگی با منوی متنوع و فضای سبز در مرکز شهر</div>

  <div class="comments-panel">
    <div class="handle-row">
      <span class="handle"></span><span class="handle-line"></span>
      <span class="comments-label">COMMENTS</span>
    </div>
    <article class="comment-card comment-card--one">
      <div class="comment-head"><span class="stars">★★★★</span><span class="place-name">Saffron Courtyard</span></div>
      <p class="comment-text">Lorem ipsum dolor sit amet, consectetur adipisicing elit, sed do eiusmod tempor incididunt ut labore et dolore magna aliqua. Ut enim ad minim veniam, quis nostrud exercitation ullamco laboris nisi ut aliquip ex ea commodo consequat. Duis aute irure dolor in reprehenderit in voluptate velit esse cillum dolore eu fugiat nulla pariatur.</p>
      <svg class="comment-pin" style="color:var(--pin-pink)"><use href="#pin-shape"/></svg>
    </article>
    <article class="comment-card comment-card--two">
      <div class="comment-head"><span class="stars">★★★★</span><span class="place-name">Saffron Courtyard</span></div>
      <p class="comment-text">Lorem ipsum dolor sit amet, consectetur adipisicing elit, sed do eiusmod tempor incididunt ut labore et dolore magna aliqua. Ut enim ad minim veniam, quis nostrud exercitation ullamco laboris nisi ut aliquip ex ea commodo consequat. Duis aute irure dolor in reprehenderit in voluptate velit esse cillum dolore eu fugiat nulla pariatur.</p>
      <svg class="comment-pin" style="color:var(--pin-blue)"><use href="#pin-shape"/></svg>
    </article>
  </div>
</section>

</body>
</html>
```